Homepage Redesign - Hi-tech business Law Firm

I'm looking for an updated graphic design (pdf file) for the homepage of dorvantlegal.ca (and which will form the general template of the other pages - but you don't need to design that). Detailed specs are in the Word file.

Deliverable is 1 pdf file that I find good looking, that sets forth the layout of the new page.

Target Market(s)

Sophisticated customers

Industry/Entity Type

Legal

Number of Pages Required

1 page

Requirements
Nice to have
• For a main background, tech type images to do with high powered boardrooms, computers, graphs, numbers, high tech manufacturing lines etc. Also, I tend to like blues and light greys, and uploaded a file today that shows my generally preferred layout, which a few of you have been getting close to.
Should not have
• Any mention of 'Personal Injury,' backgrounds that include books, or buildings with roman columns. Page should not be in dark colors or harsh on the eyes.

```html
<!DOCTYPE html>
<html lang="en">
<head>
<meta charset="utf-8">
<title>Dorvant Legal — Homepage</title>
<link href="https://fonts.googleapis.com/css2?family=Tinos:wght@400;700&family=Open+Sans:wght@400;600;700&display=swap" rel="stylesheet">
<style>
:root{
  --navy:#0c5274;
  --red:#d0170f;
  --ink:#222;
  --body:#444;
  --grey:#f1f1f1;
  --card:#f3f3f3;
  --black:#111;
  --star:#f0b400;
  --link:#1e73be;
}
*{box-sizing:border-box;margin:0;padding:0}
html,body{width:1200px;height:4402px;overflow:hidden}
body{position:relative;font-family:"Open Sans",sans-serif;color:var(--body);background:#fff;font-size:14px}
.abs{position:absolute}
.serif{font-family:"Tinos",serif}
.btn{position:absolute;background:var(--red);color:#fff;font-family:"Tinos",serif;font-size:17px;display:flex;align-items:center;justify-content:center;letter-spacing:.3px}
.ph{position:absolute}
.topbar{left:0;top:0;width:1200px;height:65px;background:var(--black);color:#fff;font-size:13px}
.topbar .item{position:absolute;display:flex;align-items:center;gap:6px}
.nav{left:0;top:65px;width:1200px;height:89px;background:var(--grey)}
.logo{display:flex;align-items:center;gap:8px}
.logo .mark{width:52px;height:52px;border:3px solid var(--navy);background:#fff}
.logo .name{font-family:"Tinos",serif;font-size:20px;letter-spacing:3px;color:#333;line-height:1.1}
.nav .links a{position:absolute;top:38px;font-size:14px;color:#333;text-decoration:none}
.hero{left:0;top:154px;width:1200px;height:606px;background:linear-gradient(180deg,#d7dce1,#eceff2 70%,#fff)}
.hero h1{position:absolute;left:111px;top:180px;font-family:"Tinos",serif;font-weight:400;font-size:41px;line-height:57px;color:#111;letter-spacing:.5px}
.hero h1 span{color:var(--navy)}
.badge{left:296px;top:675px;width:608px;height:132px;background:#fff;box-shadow:0 3px 12px rgba(0,0,0,.18);border-radius:3px}
.form{left:106px;top:897px;width:460px;height:576px;border:1.5px solid var(--navy);background:#fff;box-shadow:4px 6px 10px rgba(0,0,0,.15);border-top-right-radius:40px}
.form h3{position:absolute;left:0;width:100%;top:56px;text-align:center;font-family:"Tinos",serif;font-size:21px;color:#111;letter-spacing:.5px}
.form h3 u{text-decoration-thickness:1px}
.lbl{position:absolute;font-size:14px;color:#222}
.field{position:absolute;border-bottom:1.5px solid var(--navy);font-size:11px;color:#666;padding-bottom:3px}
.intro h2{font-family:"Tinos",serif;font-size:26px;line-height:36px;color:#111;letter-spacing:.3px}
.intro p{font-size:14px;line-height:26px;color:#444;margin-top:14px}
.practice{left:0;top:1567px;width:1200px;height:429px;background:var(--navy)}
.sec-title{position:absolute;left:0;width:1200px;text-align:center;font-family:"Tinos",serif;font-size:30px;letter-spacing:.5px}
.pcard{position:absolute;top:123px;width:231px;height:245px;border-radius:8px;overflow:hidden}
.pcard .t{position:absolute;left:0;right:0;bottom:16px;text-align:center;color:#fff;font-family:"Tinos",serif;font-weight:700;font-size:16px}
.tcard{position:absolute;width:291px;padding:26px 22px;background:var(--card)}
.tcard .who{font-family:"Tinos",serif;font-weight:700;font-size:16px;color:#111;width:160px}
.tcard .stars{color:var(--star);font-size:16px;letter-spacing:2px;margin-top:6px}
.tcard p{font-size:14px;line-height:26px;margin-top:18px;color:#444}
.tcard .av{position:absolute;right:30px;top:28px;width:74px;height:74px;border-radius:50%;background:#c9d3da;border:2px solid #fff}
.tcard.hl{background:var(--navy)}
.tcard.hl .who,.tcard.hl p{color:#fff}
.news{left:0;top:2803px;width:1200px;height:627px;background:var(--navy);overflow:hidden}
.ncard{position:absolute;top:119px;width:350px;color:#fff}
.ncard .img{width:350px;height:219px}
.ncard h4{font-family:"Tinos",serif;font-weight:400;font-size:20px;line-height:26px;margin-top:22px;width:310px}
.ncard p{font-size:14px;line-height:26px;margin-top:12px;width:330px}
.wins p{font-size:14px;line-height:26px;color:#444}
.footer{left:0;top:4011px;width:1200px;height:391px;background:var(--black);color:#fff}
.footer h5{font-family:"Open Sans",sans-serif;font-weight:400;font-size:21px}
.footer ul{list-style:none;font-size:14px;line-height:29px}
.footer .ct{font-size:14px;line-height:21px}
</style>
</head>
<body>

<div class="abs topbar">
  <div class="item" style="left:113px;top:18px">
    <svg width="12" height="16" viewBox="0 0 12 16"><path d="M6 0a6 6 0 0 0-6 6c0 4.5 6 10 6 10s6-5.5 6-10a6 6 0 0 0-6-6zm0 8.3A2.3 2.3 0 1 1 6 3.7a2.3 2.3 0 0 1 0 4.6z" fill="#fff"/></svg>
    <span style="font-size:15px">Location:</span>
    <span style="font-size:12px;line-height:18px;margin-left:6px">14 Wexley Street East, Ground Floor<br>Hamilton, ON L8R 2K4</span>
  </div>
  <div class="item" style="left:548px;top:24px">
    <svg width="15" height="12" viewBox="0 0 15 12"><rect x="1" y="1" width="13" height="10" fill="none" stroke="#fff" stroke-width="1.5"/><path d="M1 1l6.5 5.5L14 1" fill="none" stroke="#fff" stroke-width="1.5"/></svg>
    <span>adrian@dorvantlegal.ca</span>
  </div>
  <div class="item" style="left:856px;top:24px">
    <svg width="13" height="13" viewBox="0 0 16 16"><path d="M3.6 1 6 4.2 4.6 6a9 9 0 0 0 5.4 5.4l1.8-1.4L15 12.4 13.3 15C6.8 14.6 1.4 9.2 1 2.7z" fill="#fff"/></svg>
    <span>Intial Consaltation: 555.014.2290</span>
  </div>
</div>

<div class="abs nav">
  <div class="abs logo" style="left:111px;top:18px">
    <div class="mark"></div>
    <div class="name">DORVANT<br>LEGAL</div>
  </div>
  <div class="links">
    <a style="left:416px">About</a>
    <a style="left:509px">Practice Areas</a>
    <a style="left:654px">News</a>
    <a style="left:739px">Resources</a>
    <a style="left:857px">Contact</a>
  </div>
  <div class="btn" style="left:965px;top:29px;width:124px;height:36px;font-family:'Open Sans',sans-serif;font-size:14px;gap:6px">SEARCH
    <svg width="13" height="13" viewBox="0 0 14 14"><circle cx="5.5" cy="5.5" r="4.3" fill="none" stroke="#fff" stroke-width="2"/><path d="M8.7 8.7 13 13" stroke="#fff" stroke-width="2.4"/></svg>
  </div>
</div>

<section class="abs hero">
  <div class="ph" role="img" aria-label="Soft blue-grey photo of a high-tech boardroom with executives, computer screens and data graphs" style="left:0;top:0;width:820px;height:606px;background:linear-gradient(100deg,rgba(150,168,186,.55),rgba(200,212,224,.4) 55%,rgba(236,239,242,0))"></div>
  <div class="ph" role="img" aria-label="Portrait of the lead lawyer in a grey suit, arms crossed" style="left:820px;top:96px;width:380px;height:510px;background:linear-gradient(180deg,#b9b9b9,#8d8d8d 55%,#a6a6a6);border-radius:160px 160px 0 0"></div>
  <h1>WINNING MATTERS:<br>CLIENTS <span>DEPEND</span> ON ME<br>FOR IT.SHOULDN'T YOU?</h1>
  <div class="btn" style="left:111px;top:380px;width:153px;height:42px">READ MORE</div>
  <div class="btn" style="left:273px;top:380px;width:190px;height:42px">VIDEO LIBRARY</div>
</section>

<div class="abs badge">
  <div class="ph" role="img" aria-label="Peer rating certificate badge" style="left:14px;top:42px;width:178px;height:46px;background:var(--red);border-radius:3px"></div>
  <p class="abs" style="left:211px;top:20px;width:380px;font-size:14px;line-height:23px;color:#333">An excellent rating for a lawyer with some Experience. This rating indicates the attorney is widely respected by their peers for high professional achievement and ethical standards.</p>
</div>

<div class="abs form">
  <h3><u>CASE EVALUATION</u></h3>
  <p class="abs" style="left:30px;top:103px;width:400px;text-align:center;font-size:14px;line-height:26px">Fill out this form to schedule your initial consult with our lawyers.</p>
  <span class="lbl" style="left:22px;top:172px">Name</span>
  <span class="lbl" style="left:245px;top:172px">Name</span>
  <div class="field" style="left:22px;top:210px;width:182px">First Name</div>
  <div class="field" style="left:245px;top:210px;width:182px">Last Name</div>
  <span class="lbl" style="left:22px;top:253px">Email</span>
  <span class="lbl" style="left:245px;top:253px">Phone No</span>
  <div class="field" style="left:22px;top:293px;width:182px">adrian@dorvantlegal.ca</div>
  <div class="field" style="left:245px;top:293px;width:182px">555.014.2290</div>
  <span class="lbl" style="left:22px;top:349px">Case Details</span>
  <div class="field" style="left:22px;top:385px;width:405px;font-size:13px">Details</div>
  <p class="abs" style="left:30px;top:420px;width:400px;text-align:center;font-size:14px;line-height:26px;color:#333">By using this site and/or submitting this form, I agree to the <span style="color:var(--link)">Privacy Policy</span> and <span style="color:var(--link)">Terms of Use</span>.</p>
  <div class="btn" style="left:150px;top:489px;width:128px;height:41px">SEND</div>
</div>

<div class="abs intro" style="left:600px;top:924px;width:492px">
  <h2>YOUR EXPERIENCED TORONTO AND HAMILTON LAWYERS – GETTING THE RESULTS THAT MATTER.</h2>
  <p style="margin-top:20px">Dorvant Legal is a boutique litigation firm with law offices in Toronto and Hamilton. We concentrate our legal practice on complex business litigation, professional negligence (malpractice) claims, technology contracts, and insurance coverage disputes. We take an innovative approach to our client's legal problems, and are guided by the philosophy that our job is to get results.</p>
  <p style="margin-top:26px">The lawyers at Dorvant Legal have the reputation for vigorously representing their clients' interests and competing hard to obtain the best possible results. With experience at all stages of legal disputes, the lawyers at Dorvant Legal are equally at home negotiating in a boardroom or presenting a case at trial. We hope that you take the time to explore our website to find out how our record of excellence, expertise and many years of experience can assist you.</p>
</div>

<section class="abs practice">
  <h2 class="sec-title" style="top:40px;color:#fff">AREA OF PRACTICE</h2>
  <div class="pcard" style="left:111px" role="img" aria-label="Business people reviewing a contract at a desk">
    <div style="position:absolute;inset:0;background:linear-gradient(160deg,#5d6b78,#2b3540)"></div>
    <div class="t">Business Litigation</div>
  </div>
  <div class="pcard" style="left:359px;background:#3b3b3b">
    <div style="position:absolute;left:0;right:0;top:20px;text-align:center;color:#fff;font-family:'Tinos',serif;font-weight:700;font-size:16px">Construction Litigation</div>
    <p style="position:absolute;left:16px;right:16px;top:52px;text-align:center;color:#fff;font-size:14px;line-height:26px">When your insurance company refuses to pay, you need a lawyer who has experience suing insurance companies, and winning</p>
    <div style="position:absolute;left:0;right:0;top:186px;text-align:center;color:var(--red);font-family:'Tinos',serif;font-size:15px">READ MORE</div>
  </div>
  <div class="pcard" style="left:607px" role="img" aria-label="Stressed office workers, one holding her head">
    <div style="position:absolute;inset:0;background:linear-gradient(160deg,#8a8a84,#4a4a4a)"></div>
    <div class="t">Professional Negligence</div>
  </div>
  <div class="pcard" style="left:856px" role="img" aria-label="Construction workers on a job site">
    <div style="position:absolute;inset:0;background:linear-gradient(180deg,#7fa3c2,#5a6a6e 60%,#3f4a4c)"></div>
    <div class="t">Breach Of Contract</div>
  </div>
</section>

<h2 class="sec-title" style="top:2082px;color:#111">CLIENT TESTIMONIALS</h2>
<div class="tcard" style="left:111px;top:2162px;height:444px">
  <div class="who" style="margin-top:26px">Nora Whitfield</div>
  <div class="stars">★★★★★</div>
  <div class="av" role="img" aria-label="Client portrait"></div>
  <p>I cannot say enough about having Adrian Dorvant as my lawyer! I found him during a very difficult and stressful time and was so nervous about finding a good lawyer after having a few bad ex-periences. The experience that I had with Adrian eased ALL of that anxiety for me! He worked very very hard on my settlement and was very reassuring and truly cared about my situation.</p>
</div>
<div class="tcard hl" style="left:448px;top:2211px;height:445px;padding-top:20px">
  <div class="who" style="margin-top:32px">Paul &amp; Dana Rowe</div>
  <div class="stars">★★★★★</div>
  <div class="av" role="img" aria-label="Client portrait" style="width:80px;height:80px;top:20px;right:14px"></div>
  <p style="margin-top:12px">We highly recommend Adrian Dorvant, he truly comes as advertised. My Wife and I were caught in a long drawn out civil action over an asset purchase agreement that lasted almost 5 years. We had previously changed lawyers 3 times and were in a dire situation less than 2 months from trial. We needed someone who cared about their clients, was ethical, knowledgeable, dedicated, and affordable.</p>
</div>
<div class="tcard" style="left:783px;top:2162px;height:444px">
  <div class="who" style="margin-top:22px">Luis (Lou) Marrero</div>
  <div class="stars">★★★★★</div>
  <div class="av" role="img" aria-label="Client portrait"></div>
  <p>As a real estate broker we encountered a transaction where we needed the expertise of a litigation attorney to help us collect a disputed commission. The transaction was very complicated and we needed an attorney that would be extremely thorough. After interviewing several attorney's we settled on Adrian Dorvant, ESQ., as our legal representative. To our good fortune it was the best</p>
</div>
<div class="btn" style="left:528px;top:2675px;width:130px;height:39px">VIEW MORE</div>

<section class="abs news">
  <h2 class="sec-title" style="top:34px;color:#fff">LATEST NEWS</h2>
  <svg class="abs" style="left:1124px;top:77px" width="56" height="24" viewBox="0 0 56 24">
    <circle cx="12" cy="12" r="11" fill="#9aa7ae"/><path d="M14 6 8 12l6 6" fill="none" stroke="#0c5274" stroke-width="3"/>
    <circle cx="44" cy="12" r="11" fill="#fff"/><path d="M42 6l6 6-6 6" fill="none" stroke="#0c5274" stroke-width="3"/>
  </svg>
  <div class="ncard" style="left:111px">
    <div class="img" role="img" aria-label="Older man in conversation on a couch" style="background:linear-gradient(135deg,#b9b4ab,#5e5850)"></div>
    <h4>Metro Broadcast Story on Technology in the Courts</h4>
    <p>Clara Benning interviewed the Chief Justice of Ontario along with Adrian Dorvant on the efforts by the Ontario court system to modernize in the face of Covid-19.</p>
    <div class="btn" style="position:relative;margin-top:16px;width:131px;height:39px">READ MORE</div>
  </div>
  <div class="ncard" style="left:548px">
    <div class="img" role="img" aria-label="Fountain pen writing on old paper" style="background:linear-gradient(135deg,#7a6443,#2c2218)"></div>
    <h4>The Provincial Bar Council governing coalition will face serious challenges</h4>
    <p>See Adrian's Article in Counsel Quarterly discussing a number of challenges the regulator will face in its next session here.</p>
    <div class="btn" style="position:relative;margin-top:16px;width:131px;height:39px">READ MORE</div>
  </div>
  <div class="ncard" style="left:985px">
    <div class="img" role="img" aria-label="Hand signing a document" style="background:linear-gradient(135deg,#c1672c,#3a1f12)"></div>
    <h4>Provincial Bar Council mandates minimum wage</h4>
    <p>Adrian is quoted in an article on the debate over whether articling students should be paid. You can read the article here.</p>
    <div class="btn" style="position:relative;margin-top:16px;width:131px;height:39px">READ MORE</div>
  </div>
</section>

<h2 class="sec-title" style="top:3510px;color:#111">CASE WINS</h2>
<div class="abs wins" style="left:111px;top:3604px;width:456px">
  <p>Lorem ipsum dolor sit amet, consectetur adipiscing elit, eiusmod tempor incididunt ut labore et dolore magna aliqua. uis ultrices gravida. Risus commodo viverra enas accumsan lacus vel .Lorem ipsum dolor sit et, consecetur adipiscing elit, sed do eiusmod or incididunt ut labore et re magna aliqua. Quis ipsum suspendisse ultrices gravida. mmodo viverra maecenas accumsan ilisis.Lorm ipsum dolor sit amet, consectetur adipiscing elit, sed do eiusod bore olore magna aliqua. uis ipsum suspendise ultrices gravida. sed smod tempor incididunt ut labore et re magna aliqua.eiusod bore olore magna aliqua. uis ipsum suspendise ultrices gravida.</p>
</div>
<div class="btn" style="left:111px;top:3883px;width:163px;height:41px">PDF DOWNLOAD</div>
<div class="ph" role="img" aria-label="Preview of a court of appeal decision document" style="left:708px;top:3597px;width:244px;height:325px;background:#eceef0;border:6px solid #3d4147;border-top-width:16px;border-bottom-width:14px"></div>

<footer class="abs footer">
  <div class="abs logo" style="left:111px;top:36px">
    <div class="mark" style="width:48px;height:48px;border-color:#fff;background:#111"></div>
    <div class="name" style="color:#fff">DORVANT<br>LEGAL</div>
  </div>
  <p class="abs serif" style="left:111px;top:94px;font-size:12px">"Getting the results that matter!"</p>
  <p class="abs" style="left:111px;top:124px;width:480px;font-size:14px;line-height:26px">Dorvant Legal is a boutique law office concentrating in Complex Business Litigation, Professional Negligence, Technology Contracts, and Insurance Coverage Disputes. Our innovative and pugnacious approach gets results for our clients in the Greater Toronto Area. HST #412096553RT0001 <b>GTA – HAMILTON – NIAGARA</b></p>
  <div class="abs" style="left:111px;top:282px;width:22px;height:22px;border-radius:50%;background:#fff"></div>
  <div class="abs" style="left:145px;top:282px;width:22px;height:22px;border-radius:50%;background:#fff"></div>
  <p class="abs" style="left:111px;top:326px;font-size:12px">© 2023 Dorvant Legal. All Rights Reserved.</p>

  <div class="abs" style="left:650px;top:40px">
    <h5>Quick Lins</h5>
    <ul style="margin-top:14px">
      <li>Home</li><li>About</li><li>Practice Areas</li><li>News</li><li>Resources</li><li>Contact</li>
    </ul>
  </div>

  <div class="abs" style="left:843px;top:40px;width:260px">
    <h5>Contact Us</h5>
    <div class="ct" style="margin-top:18px;display:flex;gap:12px;align-items:center">
      <svg width="14" height="11" viewBox="0 0 15 12"><rect x="1" y="1" width="13" height="10" fill="none" stroke="#fff" stroke-width="1.5"/><path d="M1 1l6.5 5.5L14 1" fill="none" stroke="#fff" stroke-width="1.5"/></svg>adrian@dorvantlegal.ca</div>
    <div class="ct" style="margin-top:19px;display:flex;gap:14px;align-items:center">
      <svg width="13" height="13" viewBox="0 0 16 16"><path d="M3.6 1 6 4.2 4.6 6a9 9 0 0 0 5.4 5.4l1.8-1.4L15 12.4 13.3 15C6.8 14.6 1.4 9.2 1 2.7z" fill="#fff"/></svg>555.014.2290</div>
    <div class="ct" style="margin-top:19px;display:flex;gap:12px">
      <svg width="12" height="16" viewBox="0 0 12 16" style="flex:none;margin-top:2px"><path d="M6 0a6 6 0 0 0-6 6c0 4.5 6 10 6 10s6-5.5 6-10a6 6 0 0 0-6-6zm0 8.3A2.3 2.3 0 1 1 6 3.7a2.3 2.3 0 0 1 0 4.6z" fill="#fff"/></svg>
      <div>Hamilton Office: 14 Wexley Street E, Ground Floor Hamilton, ON L8R 2K4
        <div style="margin-top:12px">Toronto Office: 220 Ardent Street W #4100, Toronto, ON M5V 2T3</div>
        <div style="margin-top:12px">Niagara Office: 9 Calder Lane, Virgil, ON L0S 2K8 <span style="color:var(--link)">Sitemap</span></div>
      </div>
    </div>
  </div>
</footer>

</body>
</html>
```